Federal IT Consulting Company - Bridgemont Consulting Group

We're seeking a skilled web designer to create a modern, bold, and engaging WordPress website for Bridgemont Consulting Group, LLC. Our company specializes in federal IT consulting, and our name is a play on "Bridging Momentum." The website should reflect our expertise in the federal technology marketplace and position us as a trusted partner for clients navigating their IT journey.

contact: info@bridgemontgrp.com

Current Status

WordPress is already installed on our hosting account
We have an existing logo (may need modernization)

Design Requirements

Style:

Modern and visually striking design
Bold elements to convey confidence and expertise
Incorporate the concept of "bridging momentum" into the design

Features:

Modern UX sliders for dynamic content presentation
Eye-catching, high-quality images (stock photos to be sourced by the designer)
Responsive design for all devices

Color Scheme:

To be proposed by the designer, should align with our brand and convey trust and technological expertise

Logo:

Evaluate our current logo
Create a transparent background version if needed
Propose modernization if deemed necessary

Accessibility:

Ensure design elements are accessible to users with disabilities
Use high contrast ratios for text and background colors
Provide text alternatives for non-text content

Website Structure
Create the following pages, with the possibility of subpages:

Home
Services
About
Contact

Specific Page Requirements
Home Page

Striking hero section with a clear value proposition
Overview of our services
Client testimonials or trust indicators

Services Page

Detailed list of our IT consulting services
Clear explanation of how we help navigate the federal IT landscape

About Page

Company history and mission
Team highlights (if applicable)
Our approach to federal IT consulting

Contact Page

Contact form
Other contact methods (phone, email)

Technical Requirements

Fully responsive design
SEO best practices implemented
Fast loading times
Integration with necessary plugins (to be discussed)
Training on how to update and maintain the site
Full compliance with Web Content Accessibility Guidelines (WCAG) 2.1 Level AA
Adherence to Section 508 standards for federal website accessibility
Implementation of necessary features for ADA compliance
Updates

Designs look the same

Target Market(s)

US Federal Govt customers looking for IT support.

Industry/Entity Type

IT Consulting

Coding

Coded - Design and coding required

Colors
0054AA
0677BA
7BADD7
CADEEF
E8F1F8
0094D4
00A9DD
6FCCEA
C7EBF8
E9F6FB
00AB8E
00BBA5
67D7C9
C6EFE9
E9F9F6

```html
<!DOCTYPE html>
<html lang="en">
<head>
<meta charset="utf-8">
<title>Bridgemont Consulting Group – Federal IT Solutions</title>
<link rel="stylesheet" href="https://fonts.googleapis.com/css2?family=Orbitron:wght@500;600;700&family=Arimo:wght@400;600;700&display=swap">
<style>
:root{
  --navy:#0c1238;
  --navy-deep:#050a1e;
  --band:#2a3ba5;
  --sky:#00a2e0;
  --sky-soft:#1aa3dd;
  --button:#0a8fd0;
  --send:#0a7fc7;
  --ink:#1a2244;
  --text:#222a3a;
  --muted:#5b6475;
  --line:#4a5a8a;
  --white:#ffffff;
  --field:#ffffff;
  --star:#f5b400;
}
*{margin:0;padding:0;box-sizing:border-box}
html,body{width:1200px;height:4267px;overflow:hidden;background:var(--white)}
body{font-family:"Arimo",Arial,sans-serif;color:var(--text)}
.canvas{position:relative;width:1200px;height:4267px;overflow:hidden}
.abs{position:absolute}
.page-shapes{position:absolute;left:0;top:0}
.display{font-family:"Orbitron",sans-serif;font-weight:700;letter-spacing:1.5px;text-transform:uppercase}

/* top bar */
.topbar-social{top:8px;width:12px;height:12px;border:1.5px solid var(--white);border-radius:50%}
.topbar-item{top:6px;font-size:11px;color:var(--white);display:flex;align-items:center;gap:6px}

/* header */
.brand{display:flex;align-items:center;gap:10px}
.brand-mark{width:32px;height:32px;border-radius:50%;background:var(--sky)}
.brand-name{font-family:"Orbitron",sans-serif;font-weight:700;font-size:25px;letter-spacing:1px;color:var(--ink)}
.nav-link{top:45px;height:35px;line-height:35px;font-size:13.5px;color:#111;text-transform:uppercase}
.nav-link.is-active{background:#e2e2e2;width:80px;text-align:center}
.cta{left:935px;top:43px;width:162px;height:37px;background:var(--sky);color:var(--white);font-weight:700;font-size:13px;letter-spacing:1px;display:flex;align-items:center;justify-content:center;gap:8px}

/* hero */
.hero-visual{left:0;top:103px;width:1200px;height:610px;
  background:radial-gradient(circle at 78% 30%,#3f8ed0 0,#1d4f8a 18%,transparent 42%),linear-gradient(120deg,#0a1838 0%,#123466 45%,#1b4f8c 75%,#0f2e5e 100%);
  clip-path:polygon(0 0,100% 0,100% 485px,0 609px)}
.hero-title{left:103px;top:236px;font-size:35px;line-height:49px;color:var(--white)}
.hero-lede{left:103px;top:402px;width:460px;font-size:16px;line-height:29px;color:var(--white)}

/* services */
.eyebrow{font-size:16px;color:var(--sky-soft);text-transform:uppercase}
.section-title{font-size:26px;line-height:36px;color:var(--white);text-align:center}
.service-card{top:918px;width:317px;height:360px;border:1px solid var(--line);text-align:center;color:var(--white)}
.service-card svg.icon{position:absolute;left:50%;top:42px;transform:translateX(-50%)}
.service-card h3{position:absolute;top:120px;left:0;right:0;font-family:"Orbitron",sans-serif;font-weight:500;font-size:17.5px;line-height:25px;letter-spacing:.6px}
.service-card p{position:absolute;top:186px;left:36px;right:36px;font-size:12.5px;line-height:15px}
.circle-arrow{position:absolute;left:50%;top:284px;transform:translateX(-50%);width:36px;height:36px;border:1.5px solid var(--white);border-radius:50%;display:flex;align-items:center;justify-content:center}

/* about */
.about-visual{left:129px;top:1541px;width:439px;height:442px;border-radius:50%;
  background:radial-gradient(circle,#e6eef6 0,#c9dbea 52%,#5aa8e0 53%,#4a9fe0 70%,transparent 71%)}
.about-eyebrow{left:674px;top:1517px;font-size:13px;font-weight:700;color:var(--button)}
.about-title{left:669px;top:1546px;font-size:23px;line-height:32px;color:var(--ink);letter-spacing:1.5px}
.about-copy{left:669px;top:1700px;width:410px;font-size:16px;line-height:29px;color:var(--text)}
.stat{top:1870px}
.stat strong{display:block;font-size:25px;color:var(--button);font-weight:700}
.stat span{display:block;font-size:11px;line-height:13px;color:var(--text);margin-top:3px}
.btn-primary{left:674px;top:1960px;width:153px;height:48px;background:var(--button);color:var(--white);font-size:13px;font-weight:700;display:flex;align-items:center;justify-content:center}

/* testimonials */
.testimonial-title{left:0;width:1200px;top:2250px;font-size:30px;text-align:center;color:var(--white);letter-spacing:1.5px}
.testimonial-lede{left:340px;width:520px;top:2302px;font-size:16px;line-height:23px;text-align:center;color:var(--white)}
.testimonial-card{top:2384px;width:470px;height:226px;background:var(--white);border-radius:9px}
.testimonial-card .stars{position:absolute;left:26px;top:24px;font-size:13px;color:var(--star);letter-spacing:1px}
.testimonial-card h3{position:absolute;left:26px;top:53px;font-size:16px;font-weight:700;color:#111}
.testimonial-card p{position:absolute;left:26px;top:85px;width:410px;font-size:12.5px;line-height:21px;color:#333}
.author-avatar{position:absolute;left:26px;top:164px;width:32px;height:32px;background:#e4e4e4}
.author-name{position:absolute;left:72px;top:164px;font-size:12.5px;font-weight:700;color:#111}
.author-date{position:absolute;left:72px;top:185px;font-size:10px;color:var(--muted)}

/* why */
.why-title{left:108px;top:2834px;font-size:26px;line-height:36px;color:var(--ink);letter-spacing:1.5px}
.why-copy{left:108px;top:2915px;width:485px;font-size:13px;line-height:22px;color:var(--text)}
.feature{left:103px;display:flex;align-items:center;gap:12px;font-size:17px;font-weight:700;color:#111}
.why-visual{left:666px;top:2820px;width:391px;height:436px;clip-path:polygon(50% 0,100% 25%,100% 75%,50% 100%,0 75%,0 25%);background:var(--sky)}
.why-visual-inner{position:absolute;left:10px;top:11px;right:10px;bottom:11px;clip-path:polygon(50% 0,100% 25%,100% 75%,50% 100%,0 75%,0 25%);
  background:linear-gradient(150deg,#d9dfe6 0%,#b98868 40%,#8a5a40 60%,#c9cfd8 100%)}

/* contact */
.contact-title{left:108px;top:3412px;font-size:27px;line-height:37px;color:var(--white);letter-spacing:1.5px}
.contact-copy{left:105px;top:3494px;width:430px;font-size:12.5px;line-height:21px;color:var(--white)}
.contact-item{left:103px;color:var(--white);display:flex;gap:14px}
.contact-item h4{font-size:16px;font-weight:700;margin-bottom:4px}
.contact-item p{font-size:12.5px;line-height:16px}
.field{background:var(--field);height:46px;font-size:13px;color:#333;padding:15px 16px 0;border-radius:2px}
.send{left:626px;top:3747px;width:123px;height:50px;background:var(--send);color:var(--white);font-size:13px;font-weight:700;display:flex;align-items:center;justify-content:center}

/* footer */
.footer-brand .brand-name{color:var(--white)}
.footer-social{top:4086px;width:22px;height:22px;border:2px solid var(--white);border-radius:50%}
.footer-heading{top:4013px;font-size:16px;font-weight:700;color:var(--white)}
.footer-links{top:4062px;list-style:none}
.footer-links li{font-size:12.5px;color:var(--white);height:28px}
.footer-contact{left:800px;display:flex;align-items:center;gap:10px;color:var(--white);font-size:12.5px;line-height:15px}
.footer-contact .dot{width:26px;height:26px;border-radius:50%;background:var(--sky);flex:none;display:flex;align-items:center;justify-content:center}
.footer-rule{left:103px;top:4197px;width:994px;height:1px;background:#2a3266}
.copyright{left:0;width:1200px;top:4226px;text-align:center;font-size:12.5px;color:var(--white)}
</style>
</head>
<body>
<div class="canvas">

<svg class="page-shapes" width="1200" height="4267" viewBox="0 0 1200 4267" aria-hidden="true">
  <rect x="0" y="0" width="1200" height="28" fill="#0c1238"/>
  <polygon points="0,706 1200,588 1200,652 0,714" fill="#0aa6e0"/>
  <polygon points="0,713 1200,650 1200,1384 630,1417 0,1384" fill="#0c1238"/>
  <polygon points="0,2678 630,2742 0,2702" fill="#2740b5"/>
  <polygon points="0,2162 630,2096 1200,2162 1200,2690 630,2736 0,2684" fill="#0c1238"/>
  <polygon points="0,3314 480,3284 1200,3412 1200,3432 480,3310 0,3318" fill="#050a1e"/>
  <polygon points="0,3318 480,3310 1200,3432 1200,3930 0,3890" fill="#0aa0dc"/>
  <polygon points="0,3888 1200,3925 1200,4267 0,4267" fill="#0c1238"/>
  <polygon points="0,3896 1200,3934 1200,3966 0,3906" fill="#2a3ba5"/>
</svg>

<!-- Top bar -->
<div class="topbar" aria-label="Utility bar">
  <span class="abs topbar-social" style="left:110px" aria-label="Social profile"></span>
  <span class="abs topbar-social" style="left:140px" aria-label="Social profile"></span>
  <span class="abs topbar-social" style="left:172px" aria-label="Social profile"></span>
  <span class="abs topbar-item" style="left:815px">
    <svg width="12" height="12" viewBox="0 0 24 24" fill="#00a2e0"><path d="M6.6 10.8a15 15 0 006.6 6.6l2.2-2.2c.3-.3.7-.4 1-.2 1.1.4 2.3.6 3.6.6.6 0 1 .4 1 1V20c0 .6-.4 1-1 1A17 17 0 013 4c0-.6.4-1 1-1h3.5c.6 0 1 .4 1 1 0 1.3.2 2.5.6 3.6.1.3 0 .7-.2 1z"/></svg>
    (202) 555-0147
  </span>
  <span class="abs topbar-item" style="left:945px">
    <svg width="13" height="11" viewBox="0 0 24 20" fill="none" stroke="#00a2e0" stroke-width="2.4"><rect x="1" y="1" width="22" height="18"/><path d="M1 2l11 9 11-9"/></svg>
    info@bridgemontgrp.com
  </span>
</div>

<!-- Header -->
<header>
  <a class="abs brand" style="left:103px;top:38px" aria-label="Bridgemont home">
    <span class="brand-mark"></span><span class="brand-name">BRIDGEMONT</span>
  </a>
  <nav>
    <span class="abs nav-link is-active" style="left:414px">Home</span>
    <span class="abs nav-link" style="left:527px">Services</span>
    <span class="abs nav-link" style="left:656px">About Us</span>
    <span class="abs nav-link" style="left:764px">Contact</span>
  </nav>
  <a class="abs cta">GET STARTED
    <svg width="14" height="12" viewBox="0 0 14 12" fill="none" stroke="#fff" stroke-width="1.8"><path d="M1 6h11M7 1l5 5-5 5"/></svg>
  </a>
</header>

<!-- Hero -->
<section class="hero">
  <div class="abs hero-visual" role="img" aria-label="Dark blue digital data centre with glowing circuitry and a radiant data ring"></div>
  <h1 class="abs display hero-title">Technology<br>Transformation<br>&nbsp;Driven by Outcomes</h1>
  <p class="abs hero-lede">Federal IT subcontracting to guarantee high-performance technology teams and trusted, long-term partnerships</p>
</section>

<!-- Services -->
<section class="services">
  <p class="abs eyebrow" style="left:0;width:1200px;text-align:center;top:790px">Our Services</p>
  <h2 class="abs display section-title" style="left:0;width:1200px;top:814px">Explore Our Federal IT<br>Solutions</h2>

  <article class="abs service-card" style="left:103px">
    <svg class="icon" width="56" height="56" viewBox="0 0 56 56" fill="none" stroke="#1aa3dd" stroke-width="2"><circle cx="28" cy="28" r="24"/><ellipse cx="28" cy="28" rx="11" ry="24"/><path d="M4 28h48M8 16h40M8 40h40M28 4v48"/></svg>
    <h3>Digital Operations<br>&amp; IT Modernization</h3>
    <p>Lorem ipsum dolor sit amet consectetur. Turpis enim libero donec malesuada nunc nec gravida at. Leo pellentesque laoreet quisque at. Feugiat eget viverra elit congue eu malesuada dictum eget.</p>
    <span class="circle-arrow"><svg width="14" height="12" viewBox="0 0 14 12" fill="none" stroke="#fff" stroke-width="1.6"><path d="M1 6h11M7 1l5 5-5 5"/></svg></span>
  </article>

  <article class="abs service-card" style="left:441px">
    <svg class="icon" width="66" height="56" viewBox="0 0 66 56" fill="none" stroke="#1aa3dd" stroke-width="2"><rect x="2" y="2" width="62" height="46"/><path d="M2 8h62M24 54h18M33 48v6"/><path d="M12 40V30M22 40V24M32 40V32M42 40V20M52 40V28"/><path d="M10 28l12-10 10 8 10-12 12 8"/></svg>
    <h3 style="top:124px">Software, Applications<br>&amp; Analytics</h3>
    <p style="top:190px">Lorem ipsum dolor sit amet consectetur. Turpis enim libero donec malesuada nunc nec gravida at. Leo pellentesque laoreet quisque at. Feugiat eget viverra elit congue eu malesuada dictum eget.</p>
    <span class="circle-arrow" style="top:288px"><svg width="14" height="12" viewBox="0 0 14 12" fill="none" stroke="#fff" stroke-width="1.6"><path d="M1 6h11M7 1l5 5-5 5"/></svg></span>
  </article>

  <article class="abs service-card" style="left:780px">
    <svg class="icon" width="60" height="56" viewBox="0 0 60 56" fill="none" stroke="#1aa3dd" stroke-width="2"><path d="M16 24a10 10 0 0119-6 8 8 0 0115 6h2a7 7 0 010 14H38"/><rect x="4" y="22" width="22" height="8"/><rect x="4" y="32" width="22" height="8"/><rect x="4" y="42" width="22" height="8"/><rect x="32" y="38" width="14" height="14"/><path d="M26 36h6"/></svg>
    <h3>Infrastructure<br>Operations</h3>
    <p>Lorem ipsum dolor sit amet consectetur. Turpis enim libero donec malesuada nunc nec gravida at. Leo pellentesque laoreet quisque at. Feugiat eget viverra elit congue eu malesuada dictum eget.</p>
    <span class="circle-arrow"><svg width="14" height="12" viewBox="0 0 14 12" fill="none" stroke="#fff" stroke-width="1.6"><path d="M1 6h11M7 1l5 5-5 5"/></svg></span>
  </article>
</section>

<!-- About -->
<section class="about">
  <div class="abs about-visual" role="img" aria-label="Two consultants discussing a project on a tablet, framed in a blue ring"></div>
  <p class="abs about-eyebrow">ABOUT US</p>
  <h2 class="abs display about-title">Developing Innovative,<br>Mission-Focused<br>Cybersecurity and<br>Technology Solutions</h2>
  <p class="abs about-copy">Lorem ipsum dolor sit amet consectetur. Proin luctus fusce mi mauris lectus purus. Massa pretium eu vestibulum amet ac. Id nunc vitae in sapien. Penatibus scelerisque vel amet nisl convallis. Commodo mauris massa dolor nec adipiscing.</p>
  <div class="abs stat" style="left:669px"><strong>18K+</strong><span>Customer Served</span></div>
  <div class="abs stat" style="left:819px"><strong>250+</strong><span>Cyber Security<br>Experts</span></div>
  <div class="abs stat" style="left:953px"><strong>3700</strong><span>Cyber Security<br>Projects</span></div>
  <a class="abs btn-primary">Learn More</a>
</section>

<!-- Testimonials -->
<section class="testimonials">
  <h2 class="abs display testimonial-title">What Our Clients Are Saying</h2>
  <p class="abs testimonial-lede">Lorem ipsum dolor sit amet consectetur. Proin luctus fusce mi mauris lectus purus. Massa pretium eu vestibulum amet ac.</p>

  <article class="abs testimonial-card" style="left:108px">
    <span class="stars">★★★★★</span>
    <h3>Congratulation!</h3>
    <p>Lorem ipsum dolor sit amet consectetur. Commodo bibendum porta ac sed habitant ullamcorper at. Maecenas semper pulvinar ultrices morbi duis massa euismod cursus. Leo.</p>
    <span class="author-avatar"></span>
    <span class="author-name">Daniel R.</span>
    <span class="author-date">August 13, 2023</span>
  </article>

  <article class="abs testimonial-card" style="left:615px">
    <span class="stars">★★★★★</span>
    <h3>Congratulation!</h3>
    <p>Lorem ipsum dolor sit amet consectetur. Porta laoreet nunc ante sapien elit a. Pharetra eget eu morbi amet est aenean urna tincidunt nibh. Sit ac mattis lectus cras. Sed non quam.</p>
    <span class="author-avatar"></span>
    <span class="author-name">Daniel R.</span>
    <span class="author-date">August 13, 2023</span>
  </article>
</section>

<!-- Why work with us -->
<section class="why">
  <h2 class="abs display why-title">Why Work<br>With Bridgemont</h2>
  <p class="abs why-copy">We have been in the trenches working with our Federal clients executing on mission transformation strategies. We apply our deep strategy and consulting expertise and our transformation experience to help you choose the best practical strategies path for your transformation, and we work with you every step of the way to make the transformation a reality.</p>

  <div class="abs feature" style="top:3060px">
    <svg width="28" height="26" viewBox="0 0 28 26" fill="#1aa3dd"><circle cx="14" cy="6" r="4"/><circle cx="5" cy="9" r="3"/><circle cx="23" cy="9" r="3"/><path d="M7 24v-6a7 7 0 0114 0v6zM0 22v-4a5 5 0 018-4v8zM28 22v-4a5 5 0 00-8-4v8z"/></svg>
    In-depth industry knowledge and experience
  </div>
  <div class="abs feature" style="top:3113px">
    <svg width="28" height="28" viewBox="0 0 28 28" fill="none" stroke="#1aa3dd" stroke-width="2"><circle cx="14" cy="14" r="12"/><path d="M6 15l5-4 4 3 3-2 5 4M10 18l3 3 4-3"/></svg>
    Trusted partnership
  </div>
  <div class="abs feature" style="top:3168px">
    <svg width="28" height="28" viewBox="0 0 28 28" fill="none" stroke="#1aa3dd" stroke-width="2.4"><circle cx="14" cy="14" r="5"/><path d="M14 2v4M14 22v4M2 14h4M22 14h4M5.5 5.5l2.8 2.8M19.7 19.7l2.8 2.8M5.5 22.5l2.8-2.8M19.7 8.3l2.8-2.8"/><circle cx="14" cy="14" r="9"/></svg>
    End-to-end capabilities
  </div>

  <div class="abs why-visual">
    <div class="why-visual-inner" role="img" aria-label="Two smiling colleagues working together at a laptop in a bright office"></div>
  </div>
</section>

<!-- Contact -->
<section class="contact">
  <h2 class="abs display contact-title">Ready to Find Your<br>Flow?</h2>
  <p class="abs contact-copy">Federal IT leaders value improved efficiency and frictionless operations capable of scaling to meet the demands of modern missions. Ready to chart your path forward?</p>

  <div class="abs contact-item" style="top:3593px">
    <svg width="20" height="22" viewBox="0 0 20 24" fill="none" stroke="#fff" stroke-width="2"><path d="M10 22s8-7.5 8-13A8 8 0 002 9c0 5.5 8 13 8 13z"/><circle cx="10" cy="9" r="3"/></svg>
    <div><h4>Head Office</h4><p>Lorem ipsum dolor sit amet<br>consectetur. Feugiat sodales.</p></div>
  </div>
  <div class="abs contact-item" style="top:3686px">
    <svg width="22" height="18" viewBox="0 0 24 20" fill="none" stroke="#fff" stroke-width="2"><rect x="1" y="1" width="22" height="18"/><path d="M1 2l11 9 11-9"/></svg>
    <div><h4>Email</h4><p style="font-size:15px;line-height:20px">info@bridgemontgrp.com</p></div>
  </div>
  <div class="abs contact-item" style="top:3760px">
    <svg width="22" height="22" viewBox="0 0 24 24" fill="none" stroke="#fff" stroke-width="1.8"><path d="M6.6 10.8a15 15 0 006.6 6.6l2.2-2.2c.3-.3.7-.4 1-.2 1.1.4 2.3.6 3.6.6.6 0 1 .4 1 1V20c0 .6-.4 1-1 1A17 17 0 013 4c0-.6.4-1 1-1h3.5c.6 0 1 .4 1 1 0 1.3.2 2.5.6 3.6.1.3 0 .7-.2 1z"/></svg>
    <div><h4>Phone</h4><p style="font-size:15px;font-weight:700;line-height:20px">202-555-0183</p></div>
  </div>

  <form aria-label="Contact form">
    <div class="abs field" style="left:621px;top:3505px;width:226px">First name</div>
    <div class="abs field" style="left:862px;top:3505px;width:227px">Last name</div>
    <div class="abs field" style="left:621px;top:3568px;width:226px">Email</div>
    <div class="abs field" style="left:862px;top:3568px;width:227px">Phone Number</div>
    <div class="abs field" style="left:621px;top:3629px;width:468px;height:93px">Message</div>
    <div class="abs send">SEND</div>
  </form>
</section>

<!-- Footer -->
<footer>
  <a class="abs brand footer-brand" style="left:103px;top:4011px" aria-label="Bridgemont home">
    <span class="brand-mark"></span><span class="brand-name">BRIDGEMONT</span>
  </a>
  <span class="abs footer-social" style="left:114px" aria-label="Social profile"></span>
  <span class="abs footer-social" style="left:168px" aria-label="Social profile"></span>
  <span class="abs footer-social" style="left:221px" aria-label="Social profile"></span>

  <h4 class="abs footer-heading" style="left:486px">Navigation</h4>
  <ul class="abs footer-links" style="left:493px"><li>Home</li><li>Services</li><li>About</li><li>Contact</li></ul>

  <h4 class="abs footer-heading" style="left:643px">Services</h4>
  <ul class="abs footer-links" style="left:643px"><li>Home</li><li>Services</li><li>About</li><li>Contact</li></ul>

  <h4 class="abs footer-heading" style="left:800px">Contact</h4>
  <div class="abs footer-contact" style="top:4057px">
    <span class="dot"><svg width="12" height="14" viewBox="0 0 20 24" fill="none" stroke="#fff" stroke-width="2.4"><path d="M10 22s8-7.5 8-13A8 8 0 002 9c0 5.5 8 13 8 13z"/><circle cx="10" cy="9" r="3"/></svg></span>
    <span>Lorem ipsum dolor sit amet<br>consectetur. Feugiat sodales.</span>
  </div>
  <div class="abs footer-contact" style="top:4103px">
    <span class="dot"><svg width="13" height="11" viewBox="0 0 24 20" fill="none" stroke="#fff" stroke-width="2.4"><rect x="1" y="1" width="22" height="18"/><path d="M1 2l11 9 11-9"/></svg></span>
    <span>info@bridgemontgrp.com</span>
  </div>
  <div class="abs footer-contact" style="top:4146px">
    <span class="dot"><svg width="13" height="13" viewBox="0 0 24 24" fill="#fff"><path d="M6.6 10.8a15 15 0 006.6 6.6l2.2-2.2c.3-.3.7-.4 1-.2 1.1.4 2.3.6 3.6.6.6 0 1 .4 1 1V20c0 .6-.4 1-1 1A17 17 0 013 4c0-.6.4-1 1-1h3.5c.6 0 1 .4 1 1 0 1.3.2 2.5.6 3.6.1.3 0 .7-.2 1z"/></svg></span>
    <span style="font-weight:700;font-size:14px">202-555-0183</span>
  </div>

  <div class="abs footer-rule"></div>
  <p class="abs copyright">Copyright © Bridgemont 2024. All rights reserved</p>
</footer>

</div>
</body>
</html>
```